Marvane Painting Epoxy Flyer

We need a promotional flyer for a new epoxy floor coatings division of our painting company. We do epoxy garage floor coatings and paver sealing. It needs to be based on and very similar to the attached flyer. The garage floor picture needs to look more realistic, and the before and after pavers pictures should look less shiny but still a good contrast. Include attached logo

```html
<!DOCTYPE html>
<html lang="en">
<head>
<meta charset="utf-8">
<title>Marvane Painting – Garage &amp; Driveway Flyer</title>
<link rel="stylesheet" href="https://fonts.googleapis.com/css2?family=Bebas+Neue&family=Figtree:ital,wght@0,500;0,600;0,700;0,800;1,400;1,500&display=swap">
<style>
  :root{
    --green:#3a9a3f;
    --blue:#233f8f;
    --ink:#1d1d1f;
    --rule:#d9d9d9;
    --paper:#ffffff;
    --backdrop:#e4e4e4;
  }
  *{margin:0;padding:0;box-sizing:border-box}
  h1,h2,p{font-size:inherit;font-weight:inherit}
  html,body{width:1200px;height:2250px;overflow:hidden}
  body{background:var(--backdrop);position:relative;font-family:"Figtree",sans-serif;color:var(--ink)}

  .flyer{
    position:absolute;left:55px;top:353px;
    width:778px;height:1102px;
    background:var(--paper);
    transform:scale(1.4);transform-origin:0 0;
    box-shadow:0 6px 18px rgba(0,0,0,.18);
    overflow:hidden;
  }
  .abs{position:absolute}

  /* brand */
  .brand{left:32px;top:95px;display:flex;align-items:center;gap:8px;z-index:2}
  .brand-dot{width:30px;height:30px;border-radius:50%;background:var(--green);flex:none}
  .brand-name{font-family:"Figtree",sans-serif;font-weight:800;font-size:16px;color:var(--blue);letter-spacing:.3px;line-height:1;white-space:nowrap}

  /* photos */
  .photo-pair{left:239px;top:16px;width:539px;height:309px}
  .paver-before{left:19px;top:214px;width:284px;height:150px}
  .paver-after{left:19px;top:372px;width:322px;height:150px}

  .tag{font-family:"Bebas Neue",sans-serif;font-size:27px;color:#fff;line-height:35px;height:35px;padding-left:30px}
  .tag-green{background:var(--green)}
  .tag-blue{background:var(--blue)}
  .tag-top-before{left:239px;top:16px;width:116px;clip-path:polygon(0 0,100% 0,92% 100%,0 100%)}
  .tag-top-after{left:517px;top:16px;width:104px;padding-left:26px;clip-path:polygon(0 0,100% 0,92% 100%,0 100%)}
  .tag-paver-before{left:19px;top:329px;width:129px;clip-path:polygon(0 0,94% 0,100% 100%,0 100%)}
  .tag-paver-after{left:19px;top:487px;width:129px;padding-left:37px;clip-path:polygon(0 0,94% 0,100% 100%,0 100%)}

  /* headline */
  .headline{right:30px;top:352px;text-align:right}
  .headline-top{font-family:"Bebas Neue",sans-serif;font-size:57px;line-height:50px;color:var(--green);letter-spacing:.3px}
  .headline-main{font-family:"Bebas Neue",sans-serif;font-size:94px;line-height:78px;color:var(--blue);letter-spacing:.5px}
  .headline-sub{font-family:"Figtree",sans-serif;font-style:italic;font-weight:400;font-size:28px;line-height:34px;margin-top:2px;color:var(--ink)}

  /* services */
  .service-bar{top:550px;height:36px;font-family:"Bebas Neue",sans-serif;font-size:29px;line-height:38px;color:#fff}
  .service-bar-epoxy{left:0;width:355px;background:var(--green);padding-left:65px;clip-path:polygon(0 0,98.3% 0,100% 100%,0 100%)}
  .service-bar-paver{left:357px;width:421px;background:var(--blue);padding-left:38px;clip-path:polygon(0 0,100% 0,100% 100%,1.6% 100%)}

  .benefits{list-style:none;width:318px}
  .benefits-epoxy{left:64px;top:595px}
  .benefits-paver{left:394px;top:593px;width:308px}
  .benefits li{display:flex;align-items:center;gap:10px;height:36px;border-bottom:1px solid var(--rule);font-style:italic;font-weight:500;font-size:15px;color:var(--ink)}
  .benefits li:last-child{border-bottom:none}
  .tick{width:17px;height:17px;flex:none}

  /* trust strip */
  .trust-box{left:19px;top:792px;width:740px;height:108px;background:var(--blue)}
  .trust-ribbon{left:82px;top:772px;width:614px;height:41px;background:var(--green);clip-path:polygon(0 0,100% 0,98.6% 100%,1.4% 100%);
    font-family:"Bebas Neue",sans-serif;font-size:28px;line-height:43px;color:#fff;text-align:center;letter-spacing:.2px}
  .trust-items{left:19px;top:827px;width:740px;height:60px;display:flex;align-items:center}
  .trust-item{display:flex;align-items:center;gap:12px;color:#fff;font-weight:600;font-size:19px;line-height:23px;height:58px}
  .trust-item svg{flex:none}
  .trust-licensed{padding-left:45px;width:217px}
  .trust-family{padding-left:30px;width:243px;border-left:1px solid rgba(255,255,255,.5)}
  .trust-area{padding-left:20px;border-left:1px solid rgba(255,255,255,.5)}

  /* call to action */
  .cta-heading{left:69px;top:920px;width:640px;display:flex;align-items:center;gap:14px;font-family:"Bebas Neue",sans-serif;font-size:46px;line-height:48px;white-space:nowrap}
  .cta-heading .rule{flex:1;height:2px}
  .rule-blue{background:var(--blue)}
  .rule-green{background:var(--green)}
  .cta-heading .call{color:var(--blue)}
  .cta-heading .free{color:var(--green)}
  .phone{left:66px;top:962px;display:flex;align-items:center;gap:12px}
  .phone-number{font-family:"Figtree",sans-serif;font-weight:800;font-size:86px;line-height:90px;letter-spacing:-.5px;color:var(--ink)}
  .cta-tagline{left:0;width:778px;top:1044px;text-align:center;font-style:italic;font-weight:400;font-size:23px;color:var(--ink)}
</style>
</head>
<body>
<main class="flyer">

  <svg class="abs photo-pair" viewBox="0 0 539 309" role="img" aria-label="Before and after photos of a garage floor: worn stained concrete, then a speckled grey epoxy coating">
    <defs>
      <linearGradient id="concrete" x1="0" y1="0" x2="1" y2="1">
        <stop offset="0" stop-color="#7f858b"/>
        <stop offset=".5" stop-color="#a9aeb1"/>
        <stop offset="1" stop-color="#8c9296"/>
      </linearGradient>
      <linearGradient id="epoxy" x1="0" y1="0" x2="1" y2="1">
        <stop offset="0" stop-color="#8d91a4"/>
        <stop offset="1" stop-color="#a7aab9"/>
      </linearGradient>
    </defs>
    <polygon points="0,0 273,0 338,309 93,309" fill="url(#concrete)"/>
    <polygon points="283,0 539,0 539,309 347,309" fill="url(#epoxy)"/>
  </svg>

  <div class="abs brand">
    <span class="brand-dot"></span>
    <span class="brand-name">MARVANE PAINTING</span>
  </div>

  <svg class="abs paver-before" viewBox="0 0 284 150" role="img" aria-label="Faded, weathered brick pavers before sealing">
    <defs>
      <linearGradient id="paverOld" x1="0" y1="0" x2="1" y2="1">
        <stop offset="0" stop-color="#8e8e95"/>
        <stop offset=".6" stop-color="#a89597"/>
        <stop offset="1" stop-color="#8a7f7c"/>
      </linearGradient>
    </defs>
    <polygon points="0,0 254,0 284,150 0,150" fill="url(#paverOld)"/>
  </svg>

  <svg class="abs paver-after" viewBox="0 0 322 150" role="img" aria-label="Restored red brick pavers after sealing">
    <defs>
      <linearGradient id="paverNew" x1="0" y1="0" x2="1" y2="1">
        <stop offset="0" stop-color="#a8544a"/>
        <stop offset=".5" stop-color="#c47563"/>
        <stop offset="1" stop-color="#b3604f"/>
      </linearGradient>
    </defs>
    <polygon points="0,0 294,0 322,150 0,150" fill="url(#paverNew)"/>
  </svg>

  <div class="abs tag tag-green tag-top-before">BEFORE</div>
  <div class="abs tag tag-blue tag-top-after">AFTER</div>
  <div class="abs tag tag-green tag-paver-before">BEFORE</div>
  <div class="abs tag tag-blue tag-paver-after">AFTER</div>

  <header class="abs headline">
    <h1 class="headline-top">UPGRADE YOUR GARAGE</h1>
    <p class="headline-main">&amp; DRIVEWAY</p>
    <p class="headline-sub">From worn-out to like new</p>
  </header>

  <div class="abs service-bar service-bar-epoxy">EPOXY FLOOR COATINGS</div>
  <div class="abs service-bar service-bar-paver">PAVER SEALING</div>

  <ul class="abs benefits benefits-epoxy">
    <li><svg class="tick" viewBox="0 0 20 20"><circle cx="10" cy="10" r="10" fill="var(--green)"/><path d="M5.5 10.3l3 3 6-6.3" fill="none" stroke="#fff" stroke-width="2.4" stroke-linecap="round" stroke-linejoin="round"/></svg>Durable, long-lasting finish</li>
    <li><svg class="tick" viewBox="0 0 20 20"><circle cx="10" cy="10" r="10" fill="var(--green)"/><path d="M5.5 10.3l3 3 6-6.3" fill="none" stroke="#fff" stroke-width="2.4" stroke-linecap="round" stroke-linejoin="round"/></svg>Protects from sun fading</li>
    <li><svg class="tick" viewBox="0 0 20 20"><circle cx="10" cy="10" r="10" fill="var(--green)"/><path d="M5.5 10.3l3 3 6-6.3" fill="none" stroke="#fff" stroke-width="2.4" stroke-linecap="round" stroke-linejoin="round"/></svg>Helps prevent weeds &amp; sand loss</li>
    <li><svg class="tick" viewBox="0 0 20 20"><circle cx="10" cy="10" r="10" fill="var(--green)"/><path d="M5.5 10.3l3 3 6-6.3" fill="none" stroke="#fff" stroke-width="2.4" stroke-linecap="round" stroke-linejoin="round"/></svg>Easier to clean &amp; maintain</li>
  </ul>

  <ul class="abs benefits benefits-paver">
    <li><svg class="tick" viewBox="0 0 20 20"><circle cx="10" cy="10" r="10" fill="var(--blue)"/><path d="M5.5 10.3l3 3 6-6.3" fill="none" stroke="#fff" stroke-width="2.4" stroke-linecap="round" stroke-linejoin="round"/></svg>Restores color &amp; enhances appearance</li>
    <li><svg class="tick" viewBox="0 0 20 20"><circle cx="10" cy="10" r="10" fill="var(--blue)"/><path d="M5.5 10.3l3 3 6-6.3" fill="none" stroke="#fff" stroke-width="2.4" stroke-linecap="round" stroke-linejoin="round"/></svg>Protects from sun fading</li>
    <li><svg class="tick" viewBox="0 0 20 20"><circle cx="10" cy="10" r="10" fill="var(--blue)"/><path d="M5.5 10.3l3 3 6-6.3" fill="none" stroke="#fff" stroke-width="2.4" stroke-linecap="round" stroke-linejoin="round"/></svg>Helps prevent weeds &amp; sand loss</li>
    <li><svg class="tick" viewBox="0 0 20 20"><circle cx="10" cy="10" r="10" fill="var(--blue)"/><path d="M5.5 10.3l3 3 6-6.3" fill="none" stroke="#fff" stroke-width="2.4" stroke-linecap="round" stroke-linejoin="round"/></svg>Easier to clean &amp; maintain</li>
  </ul>

  <div class="abs trust-box"></div>
  <div class="abs trust-ribbon">PRACTICAL UPGRADES THAT PROTECT AND IMPROVE YOUR HOME</div>

  <div class="abs trust-items">
    <div class="trust-item trust-licensed">
      <svg width="44" height="44" viewBox="0 0 44 44"><path d="M19 4l14 5v11c0 10-6 16-14 20C11 36 5 30 5 20V9z" fill="none" stroke="#fff" stroke-width="3" stroke-linejoin="round"/><circle cx="30" cy="30" r="10" fill="#fff"/><path d="M25.5 30l3 3 6-6" fill="none" stroke="var(--blue)" stroke-width="2.6" stroke-linecap="round" stroke-linejoin="round"/></svg>
      <span>Licensed &amp;<br>Insured</span>
    </div>
    <div class="trust-item trust-family">
      <svg width="46" height="44" viewBox="0 0 46 44"><path d="M23 3l2.6 5.4 5.9.8-4.3 4.1 1 5.8L23 16.3 17.8 19l1-5.8-4.3-4.1 5.9-.8z" fill="#fff"/><path d="M10 10l1.6 3.3 3.6.5-2.6 2.5.6 3.6L10 18.2 6.8 19.9l.6-3.6-2.6-2.5 3.6-.5z" fill="#fff"/><path d="M36 10l1.6 3.3 3.6.5-2.6 2.5.6 3.6L36 18.2l-3.2 1.7.6-3.6-2.6-2.5 3.6-.5z" fill="#fff"/><path d="M3 36l8-6c3-2 6-2 9-1l8 2c2 .5 2 3 0 3.4l-8 .6 9-.5 11-6c2-1 4 1 2 3l-10 8c-3 2-6 2-9 2H8z" fill="#fff"/></svg>
      <span>Family-Owned<br>Local Business</span>
    </div>
    <div class="trust-item trust-area">
      <svg width="36" height="44" viewBox="0 0 36 44"><path d="M18 2C9.7 2 3 8.6 3 16.8 3 28 18 42 18 42s15-14 15-25.2C33 8.6 26.3 2 18 2z" fill="#fff"/><circle cx="18" cy="16.5" r="6" fill="var(--blue)"/></svg>
      <span>Serving Prescott &amp;<br>Surrounding Areas</span>
    </div>
  </div>

  <div class="abs cta-heading">
    <span class="rule rule-blue"></span>
    <h2><span class="call">CALL FOR A </span><span class="free">FREE ESTIMATE</span></h2>
    <span class="rule rule-green"></span>
  </div>

  <div class="abs phone">
    <svg width="46" height="58" viewBox="0 0 46 58"><path d="M10 3c2-1.5 4.5-1 5.7 1l5 9c1 2 .6 4.3-1.2 5.6l-3.6 2.6c1.5 6.2 5 11.5 10 15.6l3.8-2.2c1.9-1.1 4.300-.6 5.6 1.2l5.8 8.3c1.3 1.9.9 4.4-.9 5.8l-4.6 3.5C29 60 10 40 6 19c-.8-4.6.8-11.4 4-16z" fill="var(--green)"/></svg>
    <span class="phone-number">928-555-0147</span>
  </div>

  <p class="abs cta-tagline">Fast, professional service you can trust</p>

</main>
</body>
</html>
```